Webdesign für Honigmanufaktur
Zielgruppe
Imkerei, Verkauf von Honig und Honigerzeugnissen, so wie Bienenwachskerzen.
Zielgruppe sind vermutlich Frauen im mittleren bis gehobenen Alter.
Aufgabenstellung
Es gibt ein Firmenlogo.
Ich bevorzuge als Grundfarbe weiß, lasse mich aber von guten Einfällen gerne überraschen.
Die Website www.velunda.at finde ich sehr ansprechend.
Nur ohne Musik.
Ohne Deutsch/Englisch Auswahl.
Es soll danach Word press verwendet werden.

```html
<!DOCTYPE html>
<html lang="de">
<head>
<meta charset="utf-8">
<title>Imkerei Lindenhain – Webdesign</title>
<link rel="stylesheet" href="https://fonts.googleapis.com/css2?family=Oswald:wght@400;500&family=Roboto:wght@400&display=swap">
<style>
:root{
  --bg:#f2f2f2;
  --panel:#ffffff;
  --amber:#f0a020;
  --amber-pale:#fde9c6;
  --brown:#5a3418;
  --text:#4a4a4a;
  --muted:#8c8c8c;
  --line:#dcdcdc;
}
*{margin:0;padding:0;box-sizing:border-box}
html,body{width:1200px;height:3708px;overflow:hidden;background:var(--bg)}
body{position:relative;font-family:'Roboto',sans-serif;color:var(--text)}
.screen{position:absolute;left:56px;width:1088px;height:551px;background:var(--panel);box-shadow:0 1px 6px rgba(0,0,0,.08)}
.account{position:absolute;left:752px;top:6px;width:176px;font:500 6.5px 'Oswald',sans-serif;letter-spacing:1px;color:var(--muted);display:flex;gap:14px;padding-bottom:4px;border-bottom:1px solid var(--line)}
.brand{position:absolute;left:444px;top:12px;width:200px;text-align:center}
.brand-mark{display:block;width:30px;height:30px;margin:0 auto 10px;border:4px solid var(--brown);border-radius:50%}
.brand-name{font:500 11px 'Oswald',sans-serif;letter-spacing:.5px;color:var(--brown)}
.nav{position:absolute;top:76px;left:0;width:100%;height:16px}
.nav-item{position:absolute;top:0;height:16px;font:400 8px 'Oswald',sans-serif;line-height:16px;letter-spacing:1.4px;color:var(--muted);text-align:center;width:70px;margin-left:-35px}
.nav-item svg{position:absolute;left:0;top:0;width:100%;height:100%}
.nav-item span{position:relative}
.nav-item.active{color:var(--amber)}
.nav-item.pale{background:var(--amber-pale);border-radius:8px}
.rule{position:absolute;left:0;width:100%;height:1px;background:var(--line)}
.rule.head{top:91px}
.rule.foot{top:527px}
.footer{position:absolute;top:534px;left:0;width:100%;text-align:center;font-size:6.3px;letter-spacing:.6px;color:var(--muted)}
.footer u{text-decoration:underline}
.photo{position:absolute;top:114px;height:204px}
.lavender{left:209px;width:378px;background:linear-gradient(180deg,#6d7d3e 0%,#8e8fc8 35%,#a9b08a 60%,#4e6b2c 100%)}
.honey{left:634px;top:200px;width:231px;height:240px;background:radial-gradient(ellipse at 55% 45%,#d98a30 0%,#efa83e 30%,#f8d08a 52%,#fdf0da 66%,#ffffff 78%)}
.jars{left:209px;width:322px;background:linear-gradient(180deg,#ececec,#d9d9d9 60%,#e8e8e8),#eee}
.jars::after{content:"";position:absolute;left:30px;right:30px;top:70px;height:90px;background:linear-gradient(90deg,transparent 0 8%,#e6c15a 8% 30%,transparent 30% 38%,#e29624 38% 62%,transparent 62% 70%,#b85a1e 70% 92%,transparent 92%)}
.candles{left:548px;width:322px;background:linear-gradient(160deg,#e9a449,#f4c06c 45%,#d98a2c 80%,#eedfc9)}
.copy{position:absolute;top:345px;width:378px}
.copy.left{left:209px}
.copy.right{left:548px;width:322px}
.copy.small{width:322px}
.copy h2{font:500 10.5px 'Oswald',sans-serif;letter-spacing:1.2px;color:var(--amber);margin-bottom:9px}
.copy p{font-size:8.3px;line-height:13.5px;letter-spacing:.3px}
.btn{position:absolute;top:479px;width:110px;height:26px;font:400 7.5px 'Roboto',sans-serif;line-height:26px;text-align:center;letter-spacing:1.5px;color:var(--text)}
.btn svg{position:absolute;left:0;top:0;width:100%;height:100%}
.btn span{position:relative}
.btn.left{left:209px}
.btn.right{left:548px}
.btn.filled{color:#fff}
</style>
</head>
<body>

<section class="screen" style="top:56px">
  <div class="account"><span>MEIN KONTO</span><span>WARENKORB (0)</span></div>
  <div class="brand"><span class="brand-mark"></span><span class="brand-name">IMKEREI LINDENHAIN</span></div>
  <nav class="nav">
    <div class="nav-item active" style="left:243px"><svg viewBox="0 0 70 16" preserveAspectRatio="none"><polygon points="6,1 64,1 69,8 64,15 6,15 1,8" fill="none" stroke="#7a4a22" stroke-width="1.2"/></svg><span>HOME</span></div>
    <div class="nav-item" style="left:335px;width:90px;margin-left:-45px"><span>DIE MANUFAKTUR</span></div>
    <div class="nav-item" style="left:439px"><span>DER HONIG</span></div>
    <div class="nav-item" style="left:658px;width:90px;margin-left:-45px"><span>DAS BIENENWACHS</span></div>
    <div class="nav-item" style="left:755px"><span>SHOP</span></div>
    <div class="nav-item" style="left:832px"><span>KONTAKT</span></div>
  </nav>
  <div class="rule head"></div>
  <div class="photo lavender" role="img" aria-label="Foto: Biene auf Lavendelblüten"></div>
  <div class="photo honey" role="img" aria-label="Foto: Honiglöffel mit fließendem Honig"></div>
  <div class="copy left"><h2>DIE IMKEREI LINDENHAIN</h2><p>Die Imkerei Lindenhain ist eine kleine, feine Bio-Honig-Manufaktur mit dem großen Ehrgeiz, Ihnen den feinsten und besten Honig zu liefern, den Sie je gekostet haben. Lorem ipsum dolor sit amet, consetetur sadipscing elitr, sed diam nonumy eirmod tempor invidunt ut labore et dolore magna aliquyam erat, sed diam voluptua. At vero eos et accusam et justo duo dolores et ea rebum. Stet clita kasd gubergren, no sea takimata sanctus est Lorem ipsum dolor sit amet. Lorem ipsum dolor sit amet, consetetur sadipscing elitr, sed diam nonumy eirmod tempor invidunt ut labore et dolore magna aliquyam erat, sed diam voluptua.</p></div>
  <div class="rule foot"></div>
  <div class="footer">Copyright © 2018 Imkerei Lindenhain | Wabenweg 7 | 54321 Lindenfeld | Tel. 098 765 432 | info@lindenhain-honig.de | <u>Disclaimer</u> | <u>Impressum</u></div>
</section>

<section class="screen" style="top:665px">
  <div class="account"><span>MEIN KONTO</span><span>WARENKORB (0)</span></div>
  <div class="brand"><span class="brand-mark"></span><span class="brand-name">IMKEREI LINDENHAIN</span></div>
  <nav class="nav">
    <div class="nav-item active" style="left:243px"><svg viewBox="0 0 70 16" preserveAspectRatio="none"><polygon points="6,1 64,1 69,8 64,15 6,15 1,8" fill="none" stroke="#5a3418" stroke-width="1.6"/></svg><span>HOME</span></div>
    <div class="nav-item" style="left:335px;width:90px;margin-left:-45px"><span>DIE MANUFAKTUR</span></div>
    <div class="nav-item" style="left:439px"><span>DER HONIG</span></div>
    <div class="nav-item" style="left:658px;width:90px;margin-left:-45px"><span>DAS BIENENWACHS</span></div>
    <div class="nav-item" style="left:755px"><span>SHOP</span></div>
    <div class="nav-item" style="left:832px"><span>KONTAKT</span></div>
  </nav>
  <div class="rule head"></div>
  <div class="photo lavender" role="img" aria-label="Foto: Biene auf Lavendelblüten"></div>
  <div class="photo honey" role="img" aria-label="Foto: Honiglöffel mit fließendem Honig"></div>
  <div class="copy left"><h2>DIE IMKEREI LINDENHAIN</h2><p>Die Imkerei Lindenhain ist eine kleine, feine Bio-Honig-Manufaktur mit dem großen Ehrgeiz, Ihnen den feinsten und besten Honig zu liefern, den Sie je gekostet haben. Lorem ipsum dolor sit amet, consetetur sadipscing elitr, sed diam nonumy eirmod tempor invidunt ut labore et dolore magna aliquyam erat, sed diam voluptua. At vero eos et accusam et justo duo dolores et ea rebum. Stet clita kasd gubergren, no sea takimata sanctus est Lorem ipsum dolor sit amet. Lorem ipsum dolor sit amet, consetetur sadipscing elitr, sed diam nonumy eirmod tempor invidunt ut labore et dolore magna aliquyam erat, sed diam voluptua.</p></div>
  <div class="rule foot"></div>
  <div class="footer">Copyright © 2018 Imkerei Lindenhain | Wabenweg 7 | 54321 Lindenfeld | Tel. 098 765 432 | info@lindenhain-honig.de | <u>Disclaimer</u> | <u>Impressum</u></div>
</section>

<section class="screen" style="top:1273px">
  <div class="account"><span>MEIN KONTO</span><span>WARENKORB (0)</span></div>
  <div class="brand"><span class="brand-mark"></span><span class="brand-name">IMKEREI LINDENHAIN</span></div>
  <nav class="nav">
    <div class="nav-item active pale" style="left:243px"><span>HOME</span></div>
    <div class="nav-item" style="left:335px;width:90px;margin-left:-45px"><span>DIE MANUFAKTUR</span></div>
    <div class="nav-item" style="left:439px"><span>DER HONIG</span></div>
    <div class="nav-item" style="left:658px;width:90px;margin-left:-45px"><span>DAS BIENENWACHS</span></div>
    <div class="nav-item" style="left:755px"><span>SHOP</span></div>
    <div class="nav-item" style="left:832px"><span>KONTAKT</span></div>
  </nav>
  <div class="rule head"></div>
  <div class="photo lavender" role="img" aria-label="Foto: Biene auf Lavendelblüten"></div>
  <div class="photo honey" role="img" aria-label="Foto: Honiglöffel mit fließendem Honig"></div>
  <div class="copy left"><h2>DIE IMKEREI LINDENHAIN</h2><p>Die Imkerei Lindenhain ist eine kleine, feine Bio-Honig-Manufaktur mit dem großen Ehrgeiz, Ihnen den feinsten und besten Honig zu liefern, den Sie je gekostet haben. Lorem ipsum dolor sit amet, consetetur sadipscing elitr, sed diam nonumy eirmod tempor invidunt ut labore et dolore magna aliquyam erat, sed diam voluptua. At vero eos et accusam et justo duo dolores et ea rebum. Stet clita kasd gubergren, no sea takimata sanctus est Lorem ipsum dolor sit amet. Lorem ipsum dolor sit amet, consetetur sadipscing elitr, sed diam nonumy eirmod tempor invidunt ut labore et dolore magna aliquyam erat, sed diam voluptua.</p></div>
  <div class="rule foot"></div>
  <div class="footer">Copyright © 2018 Imkerei Lindenhain | Wabenweg 7 | 54321 Lindenfeld | Tel. 098 765 432 | info@lindenhain-honig.de | <u>Disclaimer</u> | <u>Impressum</u></div>
</section>

<section class="screen" style="top:1882px">
  <div class="account"><span>MEIN KONTO</span><span>WARENKORB (0)</span></div>
  <div class="brand"><span class="brand-mark"></span><span class="brand-name">IMKEREI LINDENHAIN</span></div>
  <nav class="nav">
    <div class="nav-item" style="left:243px"><span>HOME</span></div>
    <div class="nav-item" style="left:335px;width:90px;margin-left:-45px"><span>DIE MANUFAKTUR</span></div>
    <div class="nav-item" style="left:439px"><span>DER HONIG</span></div>
    <div class="nav-item" style="left:658px;width:90px;margin-left:-45px"><span>DAS BIENENWACHS</span></div>
    <div class="nav-item active" style="left:755px"><svg viewBox="0 0 70 16" preserveAspectRatio="none"><polygon points="6,1 64,1 69,8 64,15 6,15 1,8" fill="none" stroke="#7a4a22" stroke-width="1.2"/></svg><span>SHOP</span></div>
    <div class="nav-item" style="left:832px"><span>KONTAKT</span></div>
  </nav>
  <div class="rule head"></div>
  <div class="photo jars" role="img" aria-label="Foto: drei Honiggläser in verschiedenen Sorten"></div>
  <div class="photo candles" role="img" aria-label="Foto: gerollte Kerzen aus Bienenwachs"></div>
  <div class="copy left small"><h2>EXKLUSIVER HONIG AUS DEM PFÄLZERWALD</h2><p>Lorem ipsum dolor sit amet, consetetur sadipscing elitr, sed diam nonumy eirmod tempor invidunt ut labore et dolore magna aliquyam erat, sed diam voluptua. At vero eos et accusam et justo duo dolores et ea rebum. Stet clita kasd gubergren, no sea takimata sanctus est Lorem ipsum dolor sit amet. Lorem ipsum dolor sit amet, consetetur sadipscing elitr, sed diam nonumy eirmod tempor invidunt.</p></div>
  <div class="copy right"><h2>KERZEN AUS BIENENWACHS</h2><p>Lorem ipsum dolor sit amet, consetetur sadipscing elitr, sed diam nonumy eirmod tempor invidunt ut labore et dolore magna aliquyam erat, sed diam voluptua. At vero eos et accusam et justo duo dolores et ea rebum. Stet clita kasd gubergren, no sea takimata sanctus est Lorem ipsum dolor sit amet. Lorem ipsum dolor sit amet, consetetur sadipscing elitr, sed diam nonumy eirmod tempor invidunt.</p></div>
  <a class="btn left"><svg viewBox="0 0 110 26" preserveAspectRatio="none"><polygon points="8,1 102,1 109,13 102,25 8,25 1,13" fill="none" stroke="#f0a020" stroke-width="1.3"/></svg><span>JETZT KAUFEN</span></a>
  <a class="btn right"><svg viewBox="0 0 110 26" preserveAspectRatio="none"><polygon points="8,1 102,1 109,13 102,25 8,25 1,13" fill="none" stroke="#f0a020" stroke-width="1.3"/></svg><span>JETZT KAUFEN</span></a>
  <div class="rule foot"></div>
  <div class="footer">Copyright © 2018 Imkerei Lindenhain | Wabenweg 7 | 54321 Lindenfeld | Tel. 098 765 432 | info@lindenhain-honig.de | <u>Disclaimer</u> | <u>Impressum</u></div>
</section>

<section class="screen" style="top:2489px">
  <div class="account"><span>MEIN KONTO</span><span>WARENKORB (0)</span></div>
  <div class="brand"><span class="brand-mark"></span><span class="brand-name">IMKEREI LINDENHAIN</span></div>
  <nav class="nav">
    <div class="nav-item" style="left:243px"><span>HOME</span></div>
    <div class="nav-item" style="left:335px;width:90px;margin-left:-45px"><span>DIE MANUFAKTUR</span></div>
    <div class="nav-item" style="left:439px"><span>DER HONIG</span></div>
    <div class="nav-item" style="left:658px;width:90px;margin-left:-45px"><span>DAS BIENENWACHS</span></div>
    <div class="nav-item active" style="left:755px"><svg viewBox="0 0 70 16" preserveAspectRatio="none"><polygon points="6,1 64,1 69,8 64,15 6,15 1,8" fill="none" stroke="#5a3418" stroke-width="1.6"/></svg><span>SHOP</span></div>
    <div class="nav-item" style="left:832px"><span>KONTAKT</span></div>
  </nav>
  <div class="rule head"></div>
  <div class="photo jars" role="img" aria-label="Foto: drei Honiggläser in verschiedenen Sorten"></div>
  <div class="photo candles" role="img" aria-label="Foto: gerollte Kerzen aus Bienenwachs"></div>
  <div class="copy left small"><h2>EXKLUSIVER HONIG AUS DEM PFÄLZERWALD</h2><p>Lorem ipsum dolor sit amet, consetetur sadipscing elitr, sed diam nonumy eirmod tempor invidunt ut labore et dolore magna aliquyam erat, sed diam voluptua. At vero eos et accusam et justo duo dolores et ea rebum. Stet clita kasd gubergren, no sea takimata sanctus est Lorem ipsum dolor sit amet. Lorem ipsum dolor sit amet, consetetur sadipscing elitr, sed diam nonumy eirmod tempor invidunt.</p></div>
  <div class="copy right"><h2>KERZEN AUS BIENENWACHS</h2><p>Lorem ipsum dolor sit amet, consetetur sadipscing elitr, sed diam nonumy eirmod tempor invidunt ut labore et dolore magna aliquyam erat, sed diam voluptua. At vero eos et accusam et justo duo dolores et ea rebum. Stet clita kasd gubergren, no sea takimata sanctus est Lorem ipsum dolor sit amet. Lorem ipsum dolor sit amet, consetetur sadipscing elitr, sed diam nonumy eirmod tempor invidunt.</p></div>
  <a class="btn left"><svg viewBox="0 0 110 26" preserveAspectRatio="none"><polygon points="8,1 102,1 109,13 102,25 8,25 1,13" fill="none" stroke="#f0a020" stroke-width="1.3"/></svg><span>JETZT KAUFEN</span></a>
  <a class="btn right"><svg viewBox="0 0 110 26" preserveAspectRatio="none"><polygon points="8,1 102,1 109,13 102,25 8,25 1,13" fill="none" stroke="#f0a020" stroke-width="1.3"/></svg><span>JETZT KAUFEN</span></a>
  <div class="rule foot"></div>
  <div class="footer">Copyright © 2018 Imkerei Lindenhain | Wabenweg 7 | 54321 Lindenfeld | Tel. 098 765 432 | info@lindenhain-honig.de | <u>Disclaimer</u> | <u>Impressum</u></div>
</section>

<section class="screen" style="top:3096px">
  <div class="account"><span>MEIN KONTO</span><span>WARENKORB (0)</span></div>
  <div class="brand"><span class="brand-mark"></span><span class="brand-name">IMKEREI LINDENHAIN</span></div>
  <nav class="nav">
    <div class="nav-item" style="left:243px"><span>HOME</span></div>
    <div class="nav-item" style="left:335px;width:90px;margin-left:-45px"><span>DIE MANUFAKTUR</span></div>
    <div class="nav-item" style="left:439px"><span>DER HONIG</span></div>
    <div class="nav-item" style="left:658px;width:90px;margin-left:-45px"><span>DAS BIENENWACHS</span></div>
    <div class="nav-item active pale" style="left:755px"><span>SHOP</span></div>
    <div class="nav-item" style="left:832px"><span>KONTAKT</span></div>
  </nav>
  <div class="rule head"></div>
  <div class="photo jars" role="img" aria-label="Foto: drei Honiggläser in verschiedenen Sorten"></div>
  <div class="photo candles" role="img" aria-label="Foto: gerollte Kerzen aus Bienenwachs"></div>
  <div class="copy left small"><h2>EXKLUSIVER HONIG AUS DEM PFÄLZERWALD</h2><p>Lorem ipsum dolor sit amet, consetetur sadipscing elitr, sed diam nonumy eirmod tempor invidunt ut labore et dolore magna aliquyam erat, sed diam voluptua. At vero eos et accusam et justo duo dolores et ea rebum. Stet clita kasd gubergren, no sea takimata sanctus est Lorem ipsum dolor sit amet. Lorem ipsum dolor sit amet, consetetur sadipscing elitr, sed diam nonumy eirmod tempor invidunt.</p></div>
  <div class="copy right"><h2>KERZEN AUS BIENENWACHS</h2><p>Lorem ipsum dolor sit amet, consetetur sadipscing elitr, sed diam nonumy eirmod tempor invidunt ut labore et dolore magna aliquyam erat, sed diam voluptua. At vero eos et accusam et justo duo dolores et ea rebum. Stet clita kasd gubergren, no sea takimata sanctus est Lorem ipsum dolor sit amet. Lorem ipsum dolor sit amet, consetetur sadipscing elitr, sed diam nonumy eirmod tempor invidunt.</p></div>
  <a class="btn left filled"><svg viewBox="0 0 110 26" preserveAspectRatio="none"><polygon points="8,1 102,1 109,13 102,25 8,25 1,13" fill="#f0a020" stroke="#e0901a" stroke-width="1.3"/></svg><span>JETZT KAUFEN</span></a>
  <a class="btn right"><svg viewBox="0 0 110 26" preserveAspectRatio="none"><polygon points="8,1 102,1 109,13 102,25 8,25 1,13" fill="none" stroke="#f0a020" stroke-width="1.3"/></svg><span>JETZT KAUFEN</span></a>
  <div class="rule foot"></div>
  <div class="footer">Copyright © 2018 Imkerei Lindenhain | Wabenweg 7 | 54321 Lindenfeld | Tel. 098 765 432 | info@lindenhain-honig.de | <u>Disclaimer</u> | <u>Impressum</u></div>
</section>

</body>
</html>
```